Hearing Assessments & Hearing Aids

I need a business card design for my new business called 'Meridian Hearing Aids & Audiometry. I do hearing assessments for adults and children. I also fit hearing aids to hearing impaired people. I would also like to incorporate in my business card Aboriginal designs and colours with a picture of an ear which represents my hearing business as well as my Aboriginal culture.

I would also like my profession added to the business card. I am an Audioetrist.

Target Market(s)

My target customers are everyone concerned with theri hearing and for those who require hearing aids

Industry/Entity Type

Business

Contact Information for Business Card

Meridian Hearing Aids & Audiometry
Dana Forsythe
0412 309 645

Requirements
Must have
• Meridian Hearing Aids & Audiometry
Dana FOrsythe
Mobile: 0412 309 645
Email: danaforsythe07@quillmail.com

Audiometrist

```html
<!DOCTYPE html>
<html lang="en">
<head>
<meta charset="utf-8">
<title>Meridian Hearing Aids &amp; Audiometry – Business Card</title>
<link rel="stylesheet" href="https://fonts.googleapis.com/css2?family=PT+Sans:wght@400;700&display=swap">
<style>
  :root {
    --backdrop: #e4e0dd;
    --card: #fbfbfa;
    --card-edge: #d9d6d3;
    --ink: #1d1d1f;
    --accent-red: #e2233b;
    --mark-fill: #c9382e;
  }
  * { box-sizing: border-box; margin: 0; padding: 0; }
  html, body {
    width: 1200px;
    height: 840px;
    overflow: hidden;
    background: var(--backdrop);
    font-family: "PT Sans", Arial, sans-serif;
    color: var(--ink);
  }
  .canvas {
    position: relative;
    width: 1200px;
    height: 840px;
  }
  .card {
    position: absolute;
    top: 222px;
    width: 466px;
    height: 265px;
    background: var(--card);
    border: 1px solid var(--card-edge);
  }
  .card--front { left: 75px; }
  .card--back { left: 671px; }

  .brand-mark {
    position: absolute;
    left: 0;
    width: 100%;
    display: flex;
    flex-direction: column;
    align-items: center;
    gap: 10px;
  }
  .card--front .brand-mark { top: 36px; }
  .card--back .brand-mark { top: 82px; }
  .brand-mark__circle {
    width: 64px;
    height: 64px;
    border-radius: 50%;
    background: var(--mark-fill);
  }
  .brand-mark__name {
    font-size: 16px;
    font-weight: 700;
    letter-spacing: 1px;
    text-transform: uppercase;
    color: var(--ink);
  }

  .business-name {
    position: absolute;
    left: 100px;
    top: 172px;
    font-size: 13px;
    font-weight: 700;
    letter-spacing: 0.2px;
    text-transform: uppercase;
    white-space: nowrap;
  }
  .contact {
    position: absolute;
    left: 100px;
    top: 198px;
    font-size: 13px;
    line-height: 18px;
    white-space: nowrap;
  }
  .contact__divider { margin: 0 2px; }
  .contact__line {
    display: flex;
    align-items: center;
    gap: 7px;
  }
  .contact-icon { width: 9px; height: 11px; flex: none; }
</style>
</head>
<body>
<main class="canvas">
  <section class="card card--front" aria-label="Business card front">
    <div class="brand-mark">
      <span class="brand-mark__circle" aria-hidden="true"></span>
      <span class="brand-mark__name">Meridian</span>
    </div>
    <h1 class="business-name">Meridian Hearing Aids &amp; Audiometry</h1>
    <div class="contact">
      <p><span class="contact__name">Dana FOrsythe</span> <span class="contact__divider">|</span> Audiometrist</p>
      <p class="contact__line">
        <svg class="contact-icon" viewBox="0 0 9 11" aria-hidden="true">
          <rect x="1.6" y="0.6" width="5.8" height="9.8" rx="1" fill="none" stroke="var(--accent-red)" stroke-width="1.2"/>
          <rect x="3.5" y="8.2" width="2" height="1" fill="var(--accent-red)"/>
        </svg>
        <span>0412 309 645</span>
      </p>
      <p class="contact__line">
        <svg class="contact-icon" viewBox="0 0 9 11" aria-hidden="true">
          <rect x="0.6" y="2.1" width="7.8" height="6.8" rx="0.8" fill="none" stroke="var(--accent-red)" stroke-width="1.1"/>
          <path d="M0.8 2.6 L4.5 5.8 L8.2 2.6" fill="none" stroke="var(--accent-red)" stroke-width="1.1"/>
        </svg>
        <span>danaforsythe07@quillmail.com</span>
      </p>
    </div>
  </section>

  <section class="card card--back" aria-label="Business card back">
    <div class="brand-mark">
      <span class="brand-mark__circle" aria-hidden="true"></span>
      <span class="brand-mark__name">Meridian</span>
    </div>
  </section>
</main>
</body>
</html>
```